Bref créative
Stationary for telecom company
KLV Telecommunications
Professional
Dinh Quoc Bao
Director
47 Hoa Lu Street, Ward 5, Go Vap District, Ho Chi Minh City
bao.dinh@mrq.net.vn
www.klvtelecom.vn

```html
<!DOCTYPE html>
<html lang="en">
<head>
<meta charset="utf-8">
<title>KLV Telecommunications – Business Cards</title>
<link rel="stylesheet" href="https://fonts.googleapis.com/css2?family=Roboto+Condensed:wght@400;700&display=swap">
<style>
  :root {
    --page-bg: #e9ebee;
    --card-white: #ffffff;
    --card-edge: #d5d8dc;
    --brand-blue: #2c5a94;
    --band-blue-dark: #1d467d;
    --band-blue-light: #3f6faa;
    --swoosh: #141414;
    --text-light: #ffffff;
    --text-muted: #7a7f86;
  }
  * { box-sizing: border-box; margin: 0; padding: 0; }
  html, body { width: 1200px; height: 980px; overflow: hidden; }
  body {
    background: var(--page-bg);
    font-family: "Roboto Condensed", Arial, sans-serif;
    position: relative;
  }
  .card {
    position: absolute;
    left: 250px;
    width: 700px;
    height: 400px;
    border-radius: 28px;
    background: var(--card-white);
    border: 1px solid var(--card-edge);
    overflow: hidden;
  }
  .card--back { top: 60px; }
  .card--front { top: 520px; }

  .brand-name {
    color: var(--brand-blue);
    font-weight: 700;
    font-size: 40px;
    letter-spacing: 1px;
    white-space: nowrap;
  }
  .card--back .brand-name {
    position: absolute;
    top: 148px;
    width: 100%;
    text-align: center;
  }
  .web-address {
    position: absolute;
    top: 222px;
    width: 100%;
    text-align: center;
    font-size: 15px;
    letter-spacing: 7px;
    color: var(--text-muted);
  }

  .card-wave { position: absolute; inset: 0; width: 100%; height: 100%; }
  .card--front .brand-name {
    position: absolute;
    top: 88px;
    left: 0;
    width: 100%;
    text-align: center;
  }
  .contact-list {
    position: absolute;
    left: 34px;
    top: 236px;
    list-style: none;
    color: var(--text-light);
    font-size: 14px;
    line-height: 24px;
  }
  .contact-list li { display: flex; align-items: center; gap: 10px; }
  .contact-list li.contact-continued { padding-left: 24px; }
  .contact-icon { width: 14px; height: 14px; flex: none; }
  .holder {
    position: absolute;
    right: 36px;
    bottom: 34px;
    text-align: right;
    color: var(--text-light);
  }
  .holder-name { font-size: 19px; font-weight: 700; }
  .holder-title { font-size: 14px; margin-top: 2px; }
</style>
</head>
<body>

<section class="card card--back">
  <div class="brand-name">KLV Telecommunications</div>
  <div class="web-address">www.klvtelecom.vn</div>
</section>

<section class="card card--front">
  <svg class="card-wave" viewBox="0 0 700 400" preserveAspectRatio="none" aria-hidden="true">
    <defs>
      <linearGradient id="bandGradient" x1="0" y1="0" x2="1" y2="1">
        <stop offset="0" stop-color="var(--band-blue-dark)"/>
        <stop offset="1" stop-color="var(--band-blue-light)"/>
      </linearGradient>
    </defs>
    <path d="M0,212 C190,168 400,262 700,252 L700,400 L0,400 Z" fill="url(#bandGradient)"/>
    <path d="M0,196 C200,150 420,250 700,236 L700,246 C420,264 200,170 0,212 Z" fill="var(--swoosh)"/>
  </svg>

  <div class="brand-name">KLV Telecommunications</div>

  <ul class="contact-list">
    <li>
      <svg class="contact-icon" viewBox="0 0 14 14"><circle cx="7" cy="7" r="7" fill="#fff"/><path d="M7 3.2a2.3 2.3 0 0 0-2.3 2.3C4.7 7.3 7 10.6 7 10.6s2.3-3.3 2.3-5.1A2.3 2.3 0 0 0 7 3.2z" fill="var(--band-blue-dark)"/></svg>
      47 Hoa Lu Street, Ward 5, Go Vap District,
    </li>
    <li class="contact-continued">Ho Chi Minh City</li>
    <li>
      <svg class="contact-icon" viewBox="0 0 14 14"><circle cx="7" cy="7" r="7" fill="#fff"/><path d="M4.6 3.5l1.4 1.6-.7 1c.5 1 1.2 1.7 2.2 2.2l1-.7 1.6 1.4-.9 1.2C6.6 10 4 7.4 3.8 4.4z" fill="var(--band-blue-dark)"/></svg>
      (84) 8 3946 2210
    </li>
    <li>
      <svg class="contact-icon" viewBox="0 0 14 14"><circle cx="7" cy="7" r="7" fill="#fff"/><path d="M4.6 3.5l1.4 1.6-.7 1c.5 1 1.2 1.7 2.2 2.2l1-.7 1.6 1.4-.9 1.2C6.6 10 4 7.4 3.8 4.4z" fill="var(--band-blue-dark)"/></svg>
      (84) 9 0712 4583
    </li>
    <li>
      <svg class="contact-icon" viewBox="0 0 14 14"><circle cx="7" cy="7" r="7" fill="#fff"/><rect x="3.5" y="4.5" width="7" height="5" fill="none" stroke="var(--band-blue-dark)" stroke-width="1"/><path d="M3.5 4.5L7 7.3l3.5-2.8" fill="none" stroke="var(--band-blue-dark)" stroke-width="1"/></svg>
      bao.dinh@mrq.net.vn
    </li>
    <li>
      <svg class="contact-icon" viewBox="0 0 14 14"><circle cx="7" cy="7" r="7" fill="#fff"/><circle cx="7" cy="7" r="3.4" fill="none" stroke="var(--band-blue-dark)" stroke-width="1"/><path d="M3.6 7h6.8" stroke="var(--band-blue-dark)" stroke-width="0.8"/></svg>
      www.klvtelecom.vn
    </li>
  </ul>

  <div class="holder">
    <div class="holder-name">Dinh Quoc Bao</div>
    <div class="holder-title">Director</div>
  </div>
</section>

</body>
</html>
```